Quillbox package design alternate designs & color themes

We want to see different options from multiple artists for our Brand Quillbox. We are an electronic accessories company that sell everything from camera accessories to mobile device accessories. We are looking for a simple yet professional design for our packaging. Attached is one example, however we are looking for your creativity. Please use any colors / design theme that you see fit for an electronics accessory company, that blend well with the current logo.

```html
<!DOCTYPE html>
<html lang="en">
<head>
<meta charset="utf-8">
<title>Quillbox Audio Anchor Headphones Stand Package</title>
<link href="https://fonts.googleapis.com/css2?family=Oswald:wght@200;700&family=Open+Sans:wght@600;700;800&display=swap" rel="stylesheet">
<style>
  :root {
    --backdrop: #6d6d6d;
    --panel-light: #e4ece7;
    --panel-light-2: #d2ddd6;
    --brand-teal: #17977c;
    --brand-deep: #0d4d3f;
    --ink: #1a1a1a;
    --white: #ffffff;
    --photo-tone-a: #f1f3f2;
    --photo-tone-b: #c8cfcb;
  }
  * { box-sizing: border-box; margin: 0; padding: 0; }
  html, body { width: 1042px; height: 1200px; overflow: hidden; }
  body { background: var(--backdrop); position: relative; font-family: "Open Sans", sans-serif; }

  .package { position: absolute; left: 281px; top: 70px; width: 480px; height: 1060px; }

  .hang-tab {
    position: absolute; left: 80px; top: 0; width: 400px; height: 180px;
    background: var(--panel-light);
  }
  .hang-tab svg { position: absolute; left: 140px; top: 55px; }

  .spine {
    position: absolute; left: 0; top: 180px; width: 80px; height: 880px;
    background: linear-gradient(to bottom, var(--panel-light-2) 0 62%, var(--brand-teal) 62% 100%);
  }
  .spine-title {
    position: absolute; left: 24px; top: 40px; height: 470px;
    writing-mode: vertical-rl; transform: rotate(180deg);
    font-family: "Open Sans", sans-serif; font-weight: 800; font-size: 19px;
    color: var(--ink); letter-spacing: 0.5px; white-space: nowrap; text-align: end;
  }
  .spine-brand {
    position: absolute; left: 26px; top: 600px; height: 200px;
    writing-mode: vertical-rl; transform: rotate(180deg);
    font-family: "Open Sans", sans-serif; font-weight: 700; font-size: 24px;
    color: var(--brand-deep); white-space: nowrap; text-align: end;
  }

  .front {
    position: absolute; left: 80px; top: 180px; width: 400px; height: 880px;
    background: var(--panel-light); overflow: hidden;
  }
  .front-band {
    position: absolute; left: 0; top: 550px; width: 400px; height: 330px;
    background: var(--brand-teal);
  }

  .brand {
    position: absolute; left: 32px; top: 42px;
    display: flex; align-items: center; gap: 10px;
    font-family: "Open Sans", sans-serif; font-weight: 700; font-size: 34px;
    color: var(--brand-teal);
  }
  .brand-dot { width: 18px; height: 18px; border-radius: 50%; background: var(--brand-teal); }

  .product-photo {
    position: absolute; left: 150px; top: 160px; width: 240px; height: 380px;
    background: radial-gradient(ellipse at 50% 40%, var(--photo-tone-a), var(--photo-tone-b));
  }

  .product-name {
    position: absolute; left: 20px; top: 110px; height: 640px;
    writing-mode: vertical-rl; transform: rotate(180deg);
    font-family: "Oswald", sans-serif; font-size: 92px; line-height: 1;
    white-space: nowrap; text-align: start;
  }
  .product-name .word-light { font-weight: 200; color: var(--brand-deep); }
  .product-name .word-bold { font-weight: 700; color: var(--brand-teal); }

  .product-type {
    position: absolute; left: 114px; top: 440px; height: 310px;
    writing-mode: vertical-rl; transform: rotate(180deg);
    font-family: "Open Sans", sans-serif; font-weight: 700; font-size: 20px;
    letter-spacing: 2px; color: var(--white); white-space: nowrap; text-align: start;
  }

  .material-badge {
    position: absolute; left: 160px; top: 600px;
    display: flex; align-items: center; gap: 8px;
  }
  .material-badge .badge-mark {
    width: 34px; height: 34px; border-radius: 50%; border: 3px solid var(--ink);
  }
  .material-badge .badge-text {
    font-family: "Oswald", sans-serif; font-weight: 700; font-size: 17px; line-height: 0.95;
    color: var(--ink); text-transform: uppercase;
  }

  .disclaimer {
    position: absolute; right: 0; top: 690px; width: 250px; height: 34px;
    background: var(--white);
    clip-path: polygon(14px 0, 100% 0, 100% 100%, 0 100%);
    display: flex; align-items: center; padding-left: 22px;
    font-family: "Oswald", sans-serif; font-weight: 700; font-size: 14px;
    color: var(--ink); text-transform: uppercase; letter-spacing: 0.3px;
  }
</style>
</head>
<body>
  <div class="package">
    <div class="hang-tab">
      <svg width="120" height="44" viewBox="0 0 120 44" aria-hidden="true">
        <path d="M14 10 H48 A12 12 0 0 1 72 10 H106 A10 10 0 0 1 106 34 H14 A10 10 0 0 1 14 10 Z" fill="var(--backdrop)"/>
      </svg>
    </div>

    <div class="spine">
      <div class="spine-title">AUDIO ANCHOR HEADPHONES STAND</div>
      <div class="spine-brand">Quillbox</div>
    </div>

    <div class="front">
      <div class="front-band"></div>

      <div class="brand"><span class="brand-dot"></span><span>Quillbox</span></div>

      <div class="product-photo" role="img" aria-label="Photo of a black aluminium headphone stand holding a pair of silver over-ear headphones"></div>

      <div class="product-name"><span class="word-light">AUDIO</span><span class="word-bold">ANCHOR</span></div>
      <div class="product-type">HEADPHONES STAND</div>

      <div class="material-badge">
        <span class="badge-mark"></span>
        <span class="badge-text">High-Grade<br>Aluminum</span>
      </div>

      <div class="disclaimer">*Does not include headphones</div>
    </div>
  </div>
</body>
</html>
```